Recruitment website for new startup company - Calder Ashby Recruitment

Hi , I need to design a web page for my new recruitment company with the ability to link to social media accounts. The ability to add and remove job posts along with a blog page which I can update. More importantly I need the website to have the functionality of applicants being able to upload their cv and somewhere for me to store it. I will need assistance/recommendation for email address with company name, hosting and security. An about us page. The website will also need a search function for applicants to narrow down the search. Again I will need to be able to update this myself as the company grows. I have my logo ready domain address ready and would like the web site done ASAP. Thank you for your help.
Updates

Reason: Want to get a few more ideas and variations to designs done. But using logo as inspiration Thanks

Target Market(s)

Financial and property industry so professionals. New starters to senior management age range 25-60

Industry/Entity Type

Financial

Coding

Coded - Design and coding required

Number of Pages Required

4 page

Colors

Designer to choose colors to be used in the design.

Requirements
Must have
• Ability for me to add amend and remove job posts, ability for applicants to upload cv and for me to store and access it. Link to social media accounts
Should not have
• Needs to be clean approachable so not to childish but must come across as approachable and trustworthy.
• No yellow please my logo has a gold V not yellow. If it looks yellow use a different colour please. Thanks

```html
<!DOCTYPE html>
<html lang="en">
<head>
<meta charset="utf-8">
<title>Calder Ashby Recruitment</title>
<link href="https://fonts.googleapis.com/css2?family=Cinzel:wght@400;700&family=Open+Sans:wght@400;600;700&display=swap" rel="stylesheet">
<style>
:root{
  --navy:#1f3a6e;
  --navy-dark:#172c55;
  --gold:#b8953a;
  --gold-dark:#a3822d;
  --ink:#2b2b2b;
  --muted:#6b6b6b;
  --light:#f2f3f5;
  --footer:#262626;
  --white:#ffffff;
  --teal:#3fd0a6;
}
*{margin:0;padding:0;box-sizing:border-box}
html,body{width:1200px;height:3896px;overflow:hidden}
body{font-family:'Open Sans',sans-serif;color:var(--ink);background:var(--white);position:relative}
section,header,footer,.topbar{position:absolute;left:0;width:1200px}
ul{list-style:none}

/* top bar */
.topbar{top:0;height:36px;background:var(--navy);font-size:10px;color:#dfe4ee;letter-spacing:.5px}
.topbar .contact{position:absolute;left:252px;top:12px;word-spacing:2px}
.topbar .contact span{margin-right:26px}
.topbar .account{position:absolute;left:602px;top:0;width:598px;height:36px;background:var(--gold)}
.topbar .account .links{position:absolute;left:50px;top:12px;color:var(--white)}
.topbar .cv-drop{position:absolute;left:228px;top:0;height:36px;width:120px;background:var(--gold-dark);color:var(--white);font-weight:700;text-align:center;line-height:36px}

/* header */
header{top:36px;height:78px;background:var(--white)}
.brand{position:absolute;left:252px;top:18px;color:var(--navy);font-family:'Cinzel',serif;font-size:22px;font-weight:700;line-height:22px}
.brand small{display:block;font-size:12px;font-weight:400;letter-spacing:2.5px;margin-top:2px}
.nav{position:absolute;left:475px;top:31px;display:flex;gap:22px;font-family:'Cinzel',serif;font-size:11px;color:var(--ink)}
.nav .active{color:var(--navy);font-weight:700;border-bottom:2px solid var(--gold);padding-bottom:4px}
.nav-search{position:absolute;left:932px;top:28px}

/* hero */
.hero{top:114px;height:522px;background:linear-gradient(90deg,#4a4036 0%,#7b6c5e 35%,#5b5149 60%,#3a3530 100%)}
.hero .shade{position:absolute;inset:0;background:rgba(20,20,25,.35)}
.hero h1{position:absolute;top:160px;width:100%;text-align:center;color:var(--white);font-family:'Cinzel',serif;font-size:40px;letter-spacing:3px;font-weight:400}
.hero .lead{position:absolute;top:208px;width:100%;text-align:center;color:var(--white);font-family:'Cinzel',serif;font-size:22px;letter-spacing:1px}
.searchbar{position:absolute;left:260px;top:270px;width:688px;height:60px;background:rgba(255,255,255,.18);padding:12px;display:flex;gap:12px}
.select{width:160px;height:36px;background:var(--white);font-size:10px;line-height:36px;padding:0 12px;position:relative;color:var(--ink)}
.select::after{content:"";position:absolute;right:12px;top:15px;border:4px solid transparent;border-top:5px solid var(--ink)}
.searchbar .go{flex:1;background:var(--navy);color:var(--white);font-size:10px;font-weight:700;text-align:center;line-height:36px}
.arrow{position:absolute;top:240px;width:38px;height:48px;display:flex;align-items:center;justify-content:center}
.arrow.prev{left:0;background:rgba(80,80,80,.7)}
.arrow.next{right:0;background:var(--navy)}

/* steps */
.steps{top:636px;height:1226px}
.section-title{position:absolute;width:100%;text-align:center;font-family:'Cinzel',serif;font-weight:700;color:var(--navy);font-size:30px;letter-spacing:1px}
.section-sub{position:absolute;width:100%;text-align:center;font-family:'Cinzel',serif;color:var(--ink);font-size:19px;letter-spacing:1px}
.step{position:absolute;width:200px;text-align:center}
.step .disc{width:144px;height:144px;border-radius:50%;margin:0 auto;background:var(--white);border:1px solid #ececec;box-shadow:0 2px 8px rgba(0,0,0,.05);display:flex;align-items:center;justify-content:center}
.step .disc i{display:block;width:84px;height:84px;border-radius:50%}
.step h3{font-family:'Cinzel',serif;font-size:17px;color:var(--navy);letter-spacing:1.5px;margin-top:14px}
.step p{font-size:10px;line-height:15px;color:var(--muted);margin-top:8px}
.connector{position:absolute;top:241px;height:1px;background:#e1e1e1;width:100px}

.tabs{position:absolute;left:423px;top:455px;width:356px;height:42px;background:var(--navy);padding:3px;display:flex}
.tabs div{flex:1;text-align:center;line-height:36px;font-family:'Cinzel',serif;font-weight:700;font-size:12px;color:var(--white)}
.tabs .on{background:var(--gold)}

.job{position:absolute;width:337px;height:135px;background:var(--white);box-shadow:0 1px 8px rgba(0,0,0,.12);padding:16px 18px}
.job h4{font-family:'Cinzel',serif;font-size:12px;color:var(--navy);font-weight:700}
.job .loc{font-size:10px;color:var(--muted);margin-top:2px;padding-bottom:8px;border-bottom:1px solid #eee;width:215px}
.job .timer{font-size:9px;color:var(--ink);margin-top:8px;display:flex;align-items:center;gap:4px}
.job .btn{display:inline-block;margin-top:8px;background:var(--navy);color:var(--white);font-size:8px;font-weight:700;padding:6px 12px}
.job .tag{position:absolute;right:22px;top:16px;border:1px solid var(--gold);color:var(--gold);font-size:8px;padding:3px 10px}
.job .pay{position:absolute;right:22px;bottom:20px;color:var(--gold);font-size:11px}
.job .pay b{font-size:22px;font-weight:400;margin-right:4px}

.pager{position:absolute;top:1162px;left:538px;display:flex;gap:8px}
.pager span{width:24px;height:24px;border:1px solid #ddd;font-size:10px;text-align:center;line-height:22px}
.pager .on{background:var(--navy);color:var(--white);border-color:var(--navy)}

/* employer / candidate */
.split{top:1862px;height:319px;display:flex}
.split .half{width:600px;height:319px;position:relative;text-align:center;color:var(--white)}
.split .employer{background:linear-gradient(135deg,#3a3a3a,#262626)}
.split .candidate{background:linear-gradient(135deg,#4b4b4b,#2f2f2f);border-left:2px solid #555}
.split h2{font-family:'Cinzel',serif;font-size:34px;font-weight:700;letter-spacing:2px;margin-top:88px}
.split p{font-size:11px;line-height:16px;width:240px;margin:6px auto 0}
.split .cta{display:inline-block;margin-top:22px;background:var(--gold);font-family:'Cinzel',serif;font-size:11px;font-weight:700;padding:12px 18px}

/* how it works */
.how{top:2181px;height:494px;background:var(--light)}
.how .mount{position:absolute;left:0;top:140px;width:1200px;height:200px}
.how .stage{position:absolute;width:220px;text-align:center}
.how .stage i{display:block;width:144px;height:144px;border-radius:50%;margin:0 auto}
.how .stage h3{font-family:'Cinzel',serif;font-size:12px;font-weight:700;color:var(--ink);margin-top:28px;letter-spacing:.5px}
.how .stage p{font-size:10px;line-height:14px;color:var(--muted);margin-top:6px}

/* blog */
.blog{top:2675px;height:571px}
.post{position:absolute;top:177px;width:224px;height:342px;background:var(--white);box-shadow:0 1px 6px rgba(0,0,0,.14)}
.post .pic{height:170px;background:linear-gradient(135deg,#c9ced6,#8a95a5)}
.post h4{font-family:'Cinzel',serif;font-size:14px;font-weight:700;color:var(--navy);margin:16px 14px 0;line-height:17px}
.post .date{font-size:8px;color:var(--muted);margin:4px 14px 0}
.post p{font-size:10px;line-height:14px;color:var(--muted);margin:6px 14px 0}
.post .meta{position:absolute;left:0;bottom:0;width:100%;height:34px;border-top:1px solid #eee;display:flex;justify-content:space-between;align-items:center;padding:0 14px;font-size:8px;color:var(--muted)}
.post .meta b{font-family:'Cinzel',serif;font-weight:400;font-size:11px;color:var(--navy)}

/* social */
.social{top:3246px;height:156px;background:var(--navy);text-align:center}
.social h2{font-family:'Cinzel',serif;color:var(--white);font-size:30px;font-weight:700;letter-spacing:2px;margin-top:22px}
.social .row{display:flex;justify-content:center;gap:10px;margin-top:14px}
.social .row span{width:52px;height:52px;border-radius:50%;background:var(--white);display:block}

/* footer */
footer{top:3402px;height:460px;background:var(--footer);color:#cfcfcf}
.subscribe{position:absolute;left:252px;top:46px;font-family:'Cinzel',serif;font-weight:700;color:var(--white);font-size:18px;line-height:22px;letter-spacing:1px}
.email-field{position:absolute;left:473px;top:54px;width:327px;height:38px;background:var(--white);font-size:10px;color:#999;line-height:38px;padding:0 12px}
.subscribe-btn{position:absolute;left:810px;top:54px;width:140px;height:38px;background:var(--gold);color:var(--white);font-family:'Cinzel',serif;font-size:12px;font-weight:700;text-align:center;line-height:38px}
.rule{position:absolute;left:250px;top:120px;width:700px;height:1px;background:#3d3d3d}
.col{position:absolute;top:140px;font-size:9px;line-height:13px}
.col h5{font-family:'Cinzel',serif;font-size:15px;font-weight:700;color:var(--white);letter-spacing:1px;margin-bottom:12px;white-space:nowrap}
.col li{padding-left:12px;position:relative;margin-bottom:9px}
.col li::before{content:"";position:absolute;left:0;top:3px;border:3px solid transparent;border-left:4px solid #cfcfcf}
.col p{font-size:9px;line-height:13px}
.col-about{left:250px;width:185px}
.col-property{left:457px;width:215px}
.col-finance{left:691px;width:260px}
.col-finance .lists{display:flex;gap:18px}
.col-finance .lists ul:first-child{width:150px}
.col-finance .lists ul:last-child{width:92px}
.bottombar{position:absolute;left:0;top:3862px;width:1200px;height:34px;background:var(--navy);font-size:9px;color:#dfe4ee;line-height:34px;padding-left:250px}
</style>
</head>
<body>

<div class="topbar">
  <div class="contact"><span>PHONE : 0000 0000 000</span><span>EMAIL : HELLO@CALDERASHBY.CO.UK</span></div>
  <div class="account">
    <div class="links">CLIENT &nbsp;|&nbsp; REGISTER &nbsp;|&nbsp; LOGIN</div>
    <div class="cv-drop">CV DROP POINT</div>
  </div>
</div>

<header>
  <div class="brand">Calder Ashby<small>Recruitment</small></div>
  <nav class="nav">
    <span class="active">Home</span><span>About</span><span>Service</span><span>Search Jobs</span><span>Fees</span><span>Blog</span><span>Contact Us</span>
  </nav>
  <svg class="nav-search" width="16" height="16" viewBox="0 0 16 16"><circle cx="6.5" cy="6.5" r="5" fill="none" stroke="#555" stroke-width="1.6"/><line x1="10.3" y1="10.3" x2="15" y2="15" stroke="#555" stroke-width="1.8"/></svg>
</header>

<section class="hero" role="img" aria-label="Photo of two professionals reviewing documents at a desk">
  <div class="shade"></div>
  <h1>JOB SEARCH</h1>
  <div class="lead">Start looking for your new job here!</div>
  <div class="searchbar">
    <div class="select">ALL DIVISIONS</div>
    <div class="select">ALL JOB TYPES</div>
    <div class="select">ALL LOCATIONS</div>
    <div class="go">SEARCH JOBS</div>
  </div>
  <div class="arrow prev"><svg width="12" height="18" viewBox="0 0 12 18"><polyline points="9,2 3,9 9,16" fill="none" stroke="#fff" stroke-width="2"/></svg></div>
  <div class="arrow next"><svg width="12" height="18" viewBox="0 0 12 18"><polyline points="3,2 9,9 3,16" fill="none" stroke="#fff" stroke-width="2"/></svg></div>
</section>

<section class="steps">
  <h2 class="section-title" style="top:52px">ALL THE JOBS YOU IN ONE SIMPLE PLACE</h2>
  <div class="section-sub" style="top:96px">Find the jobs you want in just a few simple quicks</div>

  <div class="connector" style="left:426px"></div>
  <div class="connector" style="left:670px"></div>

  <div class="step" style="left:251px;top:170px">
    <div class="disc"><i role="img" aria-label="Magnifying glass illustration" style="background:#7fc3e6"></i></div>
    <h3>SEARCH</h3>
    <p>Lorem Ipsum is simply dummy text of the printing and typesetting industry. Lorem Ipsum has been the industry's</p>
  </div>
  <div class="step" style="left:495px;top:170px">
    <div class="disc"><i role="img" aria-label="Fountain pen illustration" style="background:#2d4a78"></i></div>
    <h3>APPLY</h3>
    <p>Lorem Ipsum is simply dummy text of the printing and typesetting industry. Lorem Ipsum has been the industry's</p>
  </div>
  <div class="step" style="left:739px;top:170px">
    <div class="disc"><i role="img" aria-label="Light bulb illustration" style="background:#f2c84b"></i></div>
    <h3>HIRED</h3>
    <p>Lorem Ipsum is simply dummy text of the printing and typesetting industry. Lorem Ipsum has been the industry's</p>
  </div>

  <div class="tabs"><div class="on">RECENT JOBS</div><div>FEATURED JOBS</div></div>

  <div class="job" style="left:250px;top:550px"><h4>SALA &amp; MARKETING COOR DINATOR</h4><div class="loc">Germany, Hanover</div><div class="timer"><svg width="9" height="9" viewBox="0 0 10 10"><circle cx="5" cy="5" r="4" fill="none" stroke="#333"/><polyline points="5,2.5 5,5 7,6" fill="none" stroke="#333"/></svg>75 Days 20 : 45 : 15</div><span class="btn">VIEW MORE</span><span class="tag">FULL TIME</span><div class="pay"><b>£</b>27500</div></div>
  <div class="job" style="left:613px;top:550px"><h4>SALA &amp; MARKETING COOR DINATOR</h4><div class="loc">Germany, Hanover</div><div class="timer"><svg width="9" height="9" viewBox="0 0 10 10"><circle cx="5" cy="5" r="4" fill="none" stroke="#333"/><polyline points="5,2.5 5,5 7,6" fill="none" stroke="#333"/></svg>75 Days 20 : 45 : 15</div><span class="btn">VIEW MORE</span><span class="tag">FULL TIME</span><div class="pay"><b>£</b>27500</div></div>
  <div class="job" style="left:250px;top:700px"><h4>SALA &amp; MARKETING COOR DINATOR</h4><div class="loc">Germany, Hanover</div><div class="timer"><svg width="9" height="9" viewBox="0 0 10 10"><circle cx="5" cy="5" r="4" fill="none" stroke="#333"/><polyline points="5,2.5 5,5 7,6" fill="none" stroke="#333"/></svg>75 Days 20 : 45 : 15</div><span class="btn">VIEW MORE</span><span class="tag">FULL TIME</span><div class="pay"><b>£</b>27500</div></div>
  <div class="job" style="left:613px;top:700px"><h4>SALA &amp; MARKETING COOR DINATOR</h4><div class="loc">Germany, Hanover</div><div class="timer"><svg width="9" height="9" viewBox="0 0 10 10"><circle cx="5" cy="5" r="4" fill="none" stroke="#333"/><polyline points="5,2.5 5,5 7,6" fill="none" stroke="#333"/></svg>75 Days 20 : 45 : 15</div><span class="btn">VIEW MORE</span><span class="tag">FULL TIME</span><div class="pay"><b>£</b>27500</div></div>
  <div class="job" style="left:250px;top:850px"><h4>SALA &amp; MARKETING COOR DINATOR</h4><div class="loc">Germany, Hanover</div><div class="timer"><svg width="9" height="9" viewBox="0 0 10 10"><circle cx="5" cy="5" r="4" fill="none" stroke="#333"/><polyline points="5,2.5 5,5 7,6" fill="none" stroke="#333"/></svg>75 Days 20 : 45 : 15</div><span class="btn">VIEW MORE</span><span class="tag">FULL TIME</span><div class="pay"><b>£</b>27500</div></div>
  <div class="job" style="left:613px;top:850px"><h4>SALA &amp; MARKETING COOR DINATOR</h4><div class="loc">Germany, Hanover</div><div class="timer"><svg width="9" height="9" viewBox="0 0 10 10"><circle cx="5" cy="5" r="4" fill="none" stroke="#333"/><polyline points="5,2.5 5,5 7,6" fill="none" stroke="#333"/></svg>75 Days 20 : 45 : 15</div><span class="btn">VIEW MORE</span><span class="tag">FULL TIME</span><div class="pay"><b>£</b>27500</div></div>
  <div class="job" style="left:250px;top:1000px"><h4>SALA &amp; MARKETING COOR DINATOR</h4><div class="loc">Germany, Hanover</div><div class="timer"><svg width="9" height="9" viewBox="0 0 10 10"><circle cx="5" cy="5" r="4" fill="none" stroke="#333"/><polyline points="5,2.5 5,5 7,6" fill="none" stroke="#333"/></svg>75 Days 20 : 45 : 15</div><span class="btn">VIEW MORE</span><span class="tag">FULL TIME</span><div class="pay"><b>£</b>27500</div></div>
  <div class="job" style="left:613px;top:1000px"><h4>SALA &amp; MARKETING COOR DINATOR</h4><div class="loc">Germany, Hanover</div><div class="timer"><svg width="9" height="9" viewBox="0 0 10 10"><circle cx="5" cy="5" r="4" fill="none" stroke="#333"/><polyline points="5,2.5 5,5 7,6" fill="none" stroke="#333"/></svg>75 Days 20 : 45 : 15</div><span class="btn">VIEW MORE</span><span class="tag">FULL TIME</span><div class="pay"><b>£</b>27500</div></div>

  <div class="pager"><span class="on">1</span><span>2</span><span>3</span><span>4</span></div>
</section>

<section class="split">
  <div class="half employer" role="img" aria-label="Dim office photo behind the employer panel">
    <h2>EMPLOYER</h2>
    <p>Lorem Ipsum is simply dummy text of the printing and typesetting industry. Lorem Ipsum has been the industry's</p>
    <span class="cta">REGISTER AS COMPANY</span>
  </div>
  <div class="half candidate" role="img" aria-label="Dim meeting photo behind the candidate panel">
    <h2>CANDIDATE</h2>
    <p>Lorem Ipsum is simply dummy text of the printing and typesetting industry. Lorem Ipsum has been the industry's</p>
    <span class="cta">REGISTER AS COMPANY</span>
  </div>
</section>

<section class="how">
  <div class="mount" role="img" aria-label="Faint mountain backdrop" style="background:linear-gradient(180deg,rgba(230,232,236,0),#e6e8ec)"></div>
  <h2 class="section-title" style="top:64px">HOW IT WORK</h2>
  <div class="section-sub" style="top:104px;font-size:15px;line-height:22px">Lorem Ipsum is simply dummy text of the printing<br>and typesetting industry.</div>
  <div class="stage" style="left:256px;top:193px"><i role="img" aria-label="Account search illustration" style="background:var(--teal)"></i><h3>REGISTER AN ACCOUNT</h3><p>Lorem Ipsum is simply dummy text of the printing and typesetting industry. Lorem Ipsum has been the industry's</p></div>
  <div class="stage" style="left:492px;top:193px"><i role="img" aria-label="Job seeker at laptop illustration" style="background:var(--gold)"></i><h3>SPECIFY &amp; SEARCH YOUR JOB</h3><p>Lorem Ipsum is simply dummy text of the printing and typesetting industry. Lorem Ipsum has been the industry's</p></div>
  <div class="stage" style="left:729px;top:193px"><i role="img" aria-label="Hand tapping apply illustration" style="background:var(--navy-dark)"></i><h3>APPLY FOR JOB</h3><p>Lorem Ipsum is simply dummy text of the printing and typesetting industry. Lorem Ipsum has been the industry's</p></div>
</section>

<section class="blog">
  <h2 class="section-title" style="top:54px">RECENT FROM BLOG</h2>
  <div class="section-sub" style="top:94px;font-size:15px;line-height:22px">Lorem Ipsum is simply dummy text of the printing<br>and typesetting industry.</div>
  <article class="post" style="left:249px">
    <div class="pic" role="img" aria-label="Photo of a business meeting"></div>
    <h4>JOB MOTIVATIONAL QUOTE</h4><div class="date">November - 20 , 2017</div>
    <p>Lorem Ipsum is simply dummy text of the printing and typesetting industry. Lorem Ipsum has been the industry's</p>
    <div class="meta"><span>Posted by : Admin</span><b>READ MORE</b></div>
  </article>
  <article class="post" style="left:488px">
    <div class="pic" role="img" aria-label="Photo of colleagues at a whiteboard" style="background:linear-gradient(135deg,#dfe6ef,#8fa3bd)"></div>
    <h4>HOW TO GET OUT OF STRESS AT WORK</h4><div class="date">November - 15 , 2017</div>
    <p>Lorem Ipsum is simply dummy text of the printing and typesetting industry. Lorem Ipsum has been the industry's</p>
    <div class="meta"><span>Posted by : Admin</span><b>READ MORE</b></div>
  </article>
  <article class="post" style="left:727px">
    <div class="pic" role="img" aria-label="Photo of a job interview at a desk" style="background:linear-gradient(135deg,#eef0f2,#b9b2a8)"></div>
    <h4>NEW JOB ON YOUR CHRISTMAS WISH LIST ?</h4><div class="date">November - 20 , 2017</div>
    <p>Lorem Ipsum is simply dummy text of the printing and typesetting industry. Lorem Ipsum has been the industry's</p>
    <div class="meta"><span>Posted by : Admin</span><b>READ MORE</b></div>
  </article>
</section>

<section class="social">
  <h2>GET SOCIAL</h2>
  <div class="row" aria-label="Social media links">
    <span title="Social link"></span><span title="Social link"></span><span title="Social link"></span><span title="Social link"></span><span title="Social link"></span><span title="Social link"></span>
  </div>
</section>

<footer>
  <div class="subscribe">SUBSCRIBE<br>TONEWSLETTERS</div>
  <div class="email-field">Your Email Address</div>
  <div class="subscribe-btn">SUBSCRIBE</div>
  <div class="rule"></div>

  <div class="col col-about">
    <h5>ABOUT US</h5>
    <p>Lorem Ipsum is simply dummy text of the printing and typesetting industry. Lorem Ipsum has been the industry's standard dummy text ever since the 1500s, when an unknown printer took</p>
    <h5 style="margin-top:22px">TARGET PERSONAS</h5>
    <ul>
      <li>Human resource managers</li>
      <li>Owners and directors of companies</li>
      <li>Smaller companies will be targeted initially, leading to larger</li>
      <li>Lenders and companies in the future</li>
    </ul>
  </div>
  <div class="col col-property">
    <h5>PROPERTY RELATED</h5>
    <ul>
      <li>Owner or manager of the estate agents</li>
      <li>HR departments of chain estate agents</li>
      <li>Individual/independent branch managers</li>
      <li>Conveyancing Solicitors and solicitors in general</li>
      <li>Estate agents</li>
      <li>Managers</li>
      <li>Front and back office staff</li>
      <li>Construction</li>
      <li>Property maintenance</li>
      <li>Commercial agents</li>
    </ul>
  </div>
  <div class="col col-finance">
    <h5>FINANCE RELATED</h5>
    <div class="lists">
      <ul>
        <li>Insurance Specialists,</li>
        <li>Mortgage advisers</li>
        <li>Financial Advisers,</li>
        <li>Financial planners/Para Planners</li>
        <li>Pension Specialists</li>
        <li>Front office staff</li>
        <li>Back Office staff</li>
        <li>Directors/managers</li>
      </ul>
      <ul>
        <li>Accountants</li>
        <li>Commercial advisers</li>
        <li>Banking</li>
        <li>Solicitors</li>
        <li>Bridging finance</li>
        <li>Equity release</li>
      </ul>
    </div>
  </div>
</footer>
<div class="bottombar">Copyright © 2017 Calder Ashby . All Rights Reserved.</div>

</body>
</html>
```